Business Card 85x40mm - Freelance audio mixing / live event operator

I am a freelance audio operator working in live events. Mostly corporate events mixing sound for a range of entertainment, awards nights and functions. I need a new card to give to perspective clients.

The final design will convey bold professionalism with a general dark vibe. Looking for dark-ish background with some smatterings of colour added.

I have attatched my old BC for an idea of what I have liked in the past. Id like a more modern updated design (that circular design on the back is not my logo it is just a picture I found that resembled sound} . For an added element possibly a mixture of some playful colours in a way that resembles an audio wave form or sound.

I have attached a photo called "audio software" with some colourful squiggly lines; maybe incorporate elements of that into into design
Updates

Added extra $ to project Damn Pixel hives fees are unreasonable

Target Market(s)

Mostly corporate clients

Industry/Entity Type

Events

Contact Information for Business Card

Corwin Pellath
Sound | FOH | Monitors | Systems | Corporate

Digital Audio Mixing Specialist, Live Event Technical Professional,

corwinpellath@mailvexo.net, +61 402 918 357

Colors
ec1f27
ffc214
9bcb3c
6b449b

Requirements
Must have
• Dark theme
• 85x40mm dimensions
Nice to have
• some sort of imagery or design to reflect audio/sound

```html
<!DOCTYPE html>
<html lang="en">
<head>
<meta charset="utf-8">
<title>Corwin Pellath — Business Card Concepts</title>
<link rel="stylesheet" href="https://fonts.googleapis.com/css2?family=Jura:wght@400;500&family=Roboto+Condensed:wght@300;400&display=swap">
<style>
  :root {
    --page: #ffffff;
    --card: #0e2a47;
    --speaker-light: #1f5479;
    --speaker-mid: #15406a;
    --ink: #ffffff;
    --divider: #8fa6bd;
    --eq-red: #e2261f;
    --eq-orange: #f47a1c;
    --eq-yellow: #ffc214;
    --eq-blue-top: #1b5d98;
    --eq-blue-bottom: #3a8bc6;
  }
  * { margin: 0; padding: 0; box-sizing: border-box; }
  html, body { width: 1200px; height: 662px; overflow: hidden; background: var(--page); }
  .sheet { position: relative; width: 1200px; height: 662px; }

  .card {
    position: absolute;
    width: 419px; height: 197px;
    background: var(--card);
    overflow: hidden;
    box-shadow: 4px 8px 14px rgba(0,0,0,0.22);
    color: var(--ink);
  }
  .card--front-a { left: 98px;  top: 110px; }
  .card--back-a  { left: 98px;  top: 335px; }
  .card--front-b { left: 674px; top: 110px; }
  .card--back-b  { left: 674px; top: 335px; }

  .speaker-art {
    position: absolute; left: -40px; top: -70px;
    width: 330px; height: 310px;
    border-radius: 50%;
    background:
      radial-gradient(ellipse 28% 30% at 38% 52%, #2a6690 0%, #184872 70%, transparent 72%),
      radial-gradient(circle at 45% 50%, var(--speaker-light) 0%, var(--speaker-mid) 55%, transparent 72%);
    opacity: 0.85;
  }

  .display { font-family: "Jura", sans-serif; font-weight: 500; letter-spacing: 0.3px; }
  .body { font-family: "Roboto Condensed", sans-serif; font-weight: 300; }

  .block-right { position: absolute; right: 35px; text-align: right; }

  .name { font-size: 20px; line-height: 1; }
  .contact { font-size: 12.5px; line-height: 16.5px; }

  .front-a-name { top: 70px; }
  .front-a-contact { top: 94px; }

  .services-line { top: 70px; font-size: 15px; white-space: nowrap; }
  .roles { top: 95px; font-size: 12.5px; line-height: 16.5px; }

  .divider { position: absolute; left: 281px; top: 0; width: 1px; background: var(--divider); }
  .card--front-b .divider { height: 146px; }
  .card--back-b .divider { height: 149px; }

  .split-left { position: absolute; right: 147px; text-align: right; }
  .split-right { position: absolute; left: 289px; }

  .front-b-contact { top: 107px; font-size: 14px; line-height: 22px; }
  .front-b-name { top: 102px; font-size: 20.5px; line-height: 23px; }

  .back-b-roles { top: 69px; font-size: 14px; line-height: 15.8px; }
  .back-b-roles .gap { display: block; height: 15.5px; }
  .back-b-services { top: 70px; font-size: 15px; line-height: 15.7px; }

  .eq { position: absolute; }
  .eq--warm { left: 251px; top: 164px; width: 134px; height: 31px; }
  .eq--cool { left: 285px; top: 155px; width: 132px; height: 37px; }
</style>
</head>
<body>
<main class="sheet">

  <svg width="0" height="0" style="position:absolute">
    <defs>
      <linearGradient id="eq-warm-fill" x1="0" y1="0" x2="0" y2="31" gradientUnits="userSpaceOnUse">
        <stop offset="0" stop-color="#e2261f"/>
        <stop offset="0.35" stop-color="#f47a1c"/>
        <stop offset="0.65" stop-color="#ffc214"/>
        <stop offset="1" stop-color="#ffc214"/>
      </linearGradient>
      <linearGradient id="eq-cool-fill" x1="0" y1="0" x2="0" y2="37" gradientUnits="userSpaceOnUse">
        <stop offset="0" stop-color="#1b5d98"/>
        <stop offset="1" stop-color="#3a8bc6"/>
      </linearGradient>
      <pattern id="eq-gaps" width="4" height="3.8" patternUnits="userSpaceOnUse">
        <rect x="0" y="2.7" width="4" height="1.1" fill="#0e2a47"/>
      </pattern>
    </defs>
  </svg>

  <!-- Front, variant A -->
  <section class="card card--front-a">
    <div class="speaker-art" role="img" aria-label="Large loudspeaker cone artwork"></div>
    <div class="block-right front-a-name display name">Corwin Pellath</div>
    <div class="block-right front-a-contact body contact">corwinpellath@mailvexo.net<br>+61 402 918 357</div>
    <svg class="eq eq--warm" viewBox="0 0 134 31" aria-hidden="true">
      <g fill="url(#eq-warm-fill)">
        <rect x="0"   y="19" width="10" height="12"/>
        <rect x="12.3" y="15" width="10" height="16"/>
        <rect x="24.6" y="0"  width="10" height="31"/>
        <rect x="36.9" y="4"  width="10" height="27"/>
        <rect x="49.2" y="11" width="10" height="20"/>
        <rect x="61.5" y="4"  width="10" height="27"/>
        <rect x="73.8" y="11" width="10" height="20"/>
        <rect x="86.1" y="0"  width="10" height="31"/>
        <rect x="98.4" y="15" width="10" height="16"/>
        <rect x="110.7" y="19" width="10" height="12"/>
        <rect x="123" y="11" width="10" height="20"/>
      </g>
      <rect width="134" height="31" fill="url(#eq-gaps)"/>
    </svg>
  </section>

  <!-- Back, variant A -->
  <section class="card card--back-a">
    <div class="speaker-art" role="img" aria-label="Large loudspeaker cone artwork"></div>
    <div class="block-right services-line display">Sound | FOH | Monitors | Systems | Corporate</div>
    <div class="block-right roles body">Digital Audio Mixing Specialist<br>Live Event Technical Professional</div>
    <svg class="eq eq--warm" viewBox="0 0 134 31" aria-hidden="true">
      <g fill="url(#eq-warm-fill)">
        <rect x="0"   y="11" width="10" height="20"/>
        <rect x="12.3" y="19" width="10" height="12"/>
        <rect x="24.6" y="11" width="10" height="20"/>
        <rect x="36.9" y="0"  width="10" height="31"/>
        <rect x="49.2" y="4"  width="10" height="27"/>
        <rect x="61.5" y="8"  width="10" height="23"/>
        <rect x="73.8" y="4"  width="10" height="27"/>
        <rect x="86.1" y="4"  width="10" height="27"/>
        <rect x="98.4" y="0"  width="10" height="31"/>
        <rect x="110.7" y="8" width="10" height="23"/>
        <rect x="123" y="11" width="10" height="20"/>
      </g>
      <rect width="134" height="31" fill="url(#eq-gaps)"/>
    </svg>
  </section>

  <!-- Front, variant B -->
  <section class="card card--front-b">
    <div class="speaker-art" role="img" aria-label="Large loudspeaker cone artwork"></div>
    <div class="split-left front-b-contact body">corwinpellath@mailvexo.net<br>+61 402 918 357</div>
    <div class="divider"></div>
    <div class="split-right front-b-name display">Corwin<br>Pellath</div>
    <svg class="eq eq--cool" viewBox="0 0 132 37" aria-hidden="true">
      <g fill="url(#eq-cool-fill)">
        <rect x="0"   y="15" width="10" height="22"/>
        <rect x="12.2" y="11" width="10" height="26"/>
        <rect x="24.4" y="0"  width="10" height="37"/>
        <rect x="36.6" y="4"  width="10" height="33"/>
        <rect x="48.8" y="11" width="10" height="26"/>
        <rect x="61"  y="4"  width="10" height="33"/>
        <rect x="73.2" y="11" width="10" height="26"/>
        <rect x="85.4" y="0"  width="10" height="37"/>
        <rect x="97.6" y="11" width="10" height="26"/>
        <rect x="109.8" y="15" width="10" height="22"/>
        <rect x="122" y="15" width="10" height="22"/>
      </g>
      <rect width="132" height="37" fill="url(#eq-gaps)"/>
    </svg>
  </section>

  <!-- Back, variant B -->
  <section class="card card--back-b">
    <div class="speaker-art" role="img" aria-label="Large loudspeaker cone artwork"></div>
    <div class="split-left back-b-roles body">Digital Audio<br>Mixing Specialist<span class="gap"></span>Live Event<br>Technical Professional</div>
    <div class="divider"></div>
    <div class="split-right back-b-services display">Sound<br>FOH<br>Monitors<br>Systems<br>Corporate</div>
    <svg class="eq eq--cool" viewBox="0 0 132 37" aria-hidden="true">
      <g fill="url(#eq-cool-fill)">
        <rect x="0"   y="19" width="10" height="18"/>
        <rect x="12.2" y="23" width="10" height="14"/>
        <rect x="24.4" y="15" width="10" height="22"/>
        <rect x="36.6" y="4"  width="10" height="33"/>
        <rect x="48.8" y="11" width="10" height="26"/>
        <rect x="61"  y="11" width="10" height="26"/>
        <rect x="73.2" y="8"  width="10" height="29"/>
        <rect x="85.4" y="8"  width="10" height="29"/>
        <rect x="97.6" y="0"  width="10" height="37"/>
        <rect x="109.8" y="11" width="10" height="26"/>
        <rect x="122" y="15" width="10" height="22"/>
      </g>
      <rect width="132" height="37" fill="url(#eq-gaps)"/>
    </svg>
  </section>

</main>
</body>
</html>
```